Torque Wizard Works LLC

We Need a business card design for a boat/car mechanic. Our thinking is to have Maybe a car on left side of card, boat on the right side of card and diagnostic computer in the middle and a cool creative way to connect all three together. We are also open to other ideas as well!
Would like for back of business card to have the contact info on it “Dorian Kelleway, text is best as the contact method 803-555-0192”

```html
<!DOCTYPE html>
<html lang="en">
<head>
<meta charset="utf-8">
<title>Dorian Kelleway – Business Card</title>
<link href="https://fonts.googleapis.com/css2?family=Mulish:wght@700;800&display=swap" rel="stylesheet">
<style>
  :root {
    --page: #d6d6d6;
    --card-white: #ffffff;
    --card-dark: #141414;
    --panel-left: #111111;
    --panel-mid: #262626;
    --panel-right: #1c1c1c;
    --frame-blue: #2f8ad6;
    --band-blue: #3a8fd0;
    --name-blue: #1d6a9c;
    --ink: #232323;
    --boat-tone-a: #8a6a4c;
    --boat-tone-b: #b9c6c8;
    --diag-tone-a: #5d7592;
    --diag-tone-b: #6b6f76;
    --car-tone-a: #2bb3ae;
    --car-tone-b: #237f8c;
  }
  * { box-sizing: border-box; margin: 0; padding: 0; }
  html, body { width: 1200px; height: 1018px; overflow: hidden; }
  body {
    background: var(--page);
    font-family: "Mulish", sans-serif;
    position: relative;
  }
  .card {
    position: absolute;
    left: 220px;
    width: 760px;
    height: 434px;
    box-shadow: 0 10px 30px rgba(0,0,0,0.18);
    overflow: hidden;
  }
  .card-front { top: 45px; background: var(--card-dark); }
  .card-back { top: 539px; background: var(--card-white); }

  /* front: three service panels */
  .service-panels {
    position: absolute; inset: 0;
    display: grid;
    grid-template-columns: 1fr 1fr 1fr;
  }
  .panel { position: relative; padding: 60px 34px; }
  .panel-boat { background: var(--panel-left); }
  .panel-diagnostics { background: var(--panel-mid); }
  .panel-car { background: var(--panel-right); }
  .art { display: block; width: 100%; height: 100%; }
  .art-boat { background: linear-gradient(160deg, var(--boat-tone-b), var(--boat-tone-a)); }
  .art-diagnostics { background: linear-gradient(160deg, var(--diag-tone-a), var(--diag-tone-b)); }
  .art-car { background: linear-gradient(160deg, var(--car-tone-a), var(--car-tone-b)); }
  .card-frame {
    position: absolute; inset: 22px;
    border: 2px solid var(--frame-blue);
    pointer-events: none;
  }

  /* back: contact */
  .contact-name {
    position: absolute; top: 74px; left: 0; right: 0;
    text-align: center;
    color: var(--name-blue);
    font-weight: 800; font-size: 50px; letter-spacing: 1px;
    line-height: 1.1;
    text-transform: uppercase;
  }
  .contact-band {
    position: absolute; left: 24px; right: 24px; top: 168px; height: 84px;
    background: var(--band-blue);
    display: flex; align-items: center; justify-content: center;
  }
  .phone-icon { width: 58px; height: 58px; }
  .contact-phone {
    position: absolute; top: 274px; left: 0; right: 0;
    text-align: center;
    color: var(--ink);
    font-weight: 800; font-size: 66px; letter-spacing: 2px;
    line-height: 1.1;
  }
</style>
</head>
<body>
  <section class="card card-front" aria-label="Card front">
    <div class="service-panels">
      <div class="panel panel-boat">
        <span class="art art-boat" role="img" aria-label="Illustration of a boat seen from above"></span>
      </div>
      <div class="panel panel-diagnostics">
        <span class="art art-diagnostics" role="img" aria-label="Photo of a rugged diagnostic laptop with cables and interface module"></span>
      </div>
      <div class="panel panel-car">
        <span class="art art-car" role="img" aria-label="Illustration of a teal car seen from above"></span>
      </div>
    </div>
    <div class="card-frame"></div>
  </section>

  <section class="card card-back" aria-label="Card back">
    <div class="card-frame"></div>
    <h1 class="contact-name">Dorian Kelleway</h1>
    <div class="contact-band">
      <svg class="phone-icon" viewBox="0 0 58 58" aria-hidden="true">
        <circle cx="29" cy="29" r="26" fill="none" stroke="#ffffff" stroke-width="3"/>
        <path d="M21 18c2-1 3 0 4 2l2 4c.6 1.4 0 2.4-1 3l-1.5 1c1 2.6 3 4.8 5.6 6l1-1.5c.8-1 1.8-1.4 3-.8l4 2c1.6.8 2 2.2 1 4-1.4 2.4-4 3.6-7 2.6C26 38 20 32 18.4 25c-.7-3 .4-5.6 2.6-7z" fill="#ffffff"/>
        <path d="M33 19a9 9 0 0 1 7 7M33 14a14 14 0 0 1 12 12" fill="none" stroke="#ffffff" stroke-width="2.4" stroke-linecap="round"/>
      </svg>
    </div>
    <p class="contact-phone">803-555-0192</p>
  </section>
</body>
</html>
```